Flyer Design

We are a property company and need attractive flyers that will grab peoples attention. We want them to be bold but simple and not too busy. I attach a draft and also our logo. We will print in A5 size.
Thank you & I look forward to receiving designs.

Industry/Entity Type

It Company

```html
<!DOCTYPE html>
<html lang="en">
<head>
<meta charset="utf-8">
<title>Orla Developments – Subdivision Flyer</title>
<link rel="stylesheet" href="https://fonts.googleapis.com/css2?family=Oswald:wght@600&family=Arimo:wght@400;700&display=swap">
<style>
  :root {
    --page-bg: #2a2a2a;
    --red: #e8313a;
    --yellow: #fdca2e;
    --green: #38b556;
    --white: #ffffff;
    --ink: #1f1f1f;
    --ink-soft: #2e3a2f;
    --photo-light: #d9d9d9;
    --photo-mid: #7a7a7a;
    --photo-dark: #3e3e3e;
  }
  * { margin: 0; padding: 0; box-sizing: border-box; }
  html, body {
    width: 1200px; height: 1010px; overflow: hidden;
    background: var(--page-bg);
  }
  .flyer {
    position: absolute; left: 264px; top: 30px;
    width: 672px; height: 950px;
    background: var(--green);
    overflow: hidden;
    font-family: "Arimo", Arial, sans-serif;
  }
  .band { position: absolute; left: 0; right: 0; }
  .band--red { top: 0; height: 370px; background: var(--red); }
  .band--yellow { top: 370px; height: 92px; background: var(--yellow); }
  .band--green { top: 462px; bottom: 0; background: var(--green); }

  .photo {
    position: absolute; left: 0; top: 0; width: 340px; height: 950px;
    clip-path: polygon(0 0, 270px 0, 300px 40px, 340px 950px, 0 950px);
    background: linear-gradient(90deg, var(--photo-light) 0%, var(--photo-light) 22%, var(--photo-mid) 40%, var(--photo-dark) 75%, var(--photo-mid) 100%);
  }

  .content { position: absolute; left: 335px; right: 28px; }
  .headline {
    font-family: "Oswald", "Arial Narrow", sans-serif;
    font-weight: 600; color: var(--white);
    font-size: 29px; line-height: 1.18;
  }
  .headline--lead { top: 48px; }
  .headline--question { top: 258px; }

  .specialty {
    top: 384px;
    font-weight: 700; color: var(--ink);
    font-size: 20px; line-height: 1.2;
  }

  .brand {
    top: 560px; text-align: center;
    font-size: 22px; letter-spacing: 2px; text-transform: uppercase;
    color: var(--ink-soft);
  }
  .contact { top: 660px; color: var(--white); }
  .contact__phone { font-size: 28px; line-height: 1.1; }
  .contact__email { font-size: 17px; margin-top: 2px; }
  .note {
    top: 740px; color: var(--ink-soft);
    font-size: 17px; line-height: 1.4;
  }
  .website {
    top: 880px; color: var(--ink-soft);
    font-size: 17px; text-align: center;
  }
</style>
</head>
<body>
  <main class="flyer">
    <div class="band band--red"></div>
    <div class="band band--yellow"></div>
    <div class="band band--green"></div>

    <div class="photo" role="img" aria-label="Black and white photo of a man in a grey suit with his hand in his pocket"></div>

    <h1 class="content headline headline--lead">Are you a homeowner looking for financial freedom while been able to keep your own home?</h1>
    <h2 class="content headline headline--question">Are you struggling to pay your mortgage?</h2>

    <p class="content specialty">Orla specialise in subdivisions including finance and management.</p>

    <p class="content brand">Orla Developments</p>

    <div class="content contact">
      <p class="contact__phone">Call 021 555 0142</p>
      <p class="contact__email">info@orlasubdivision.com</p>
    </div>

    <p class="content note">for more information<br>or to find out ifyour property<br>is suitable for subdivision<br>in Auckland.</p>

    <p class="content website">www.orlasubdivision.com</p>
  </main>
</body>
</html>
```